Business cards, envelopes and letterhead
Simple but professional
Business cards, envelopes and letterhead -
Creative Brief
Professional
Martin Doyle
President & CEO
4273 Beldon Street Chilliwack, BC V4K 7N2 Canada
mdoyle@fernobrix.com
www.fernobrix.com
On the back, we want at least the logo (maybe the styled water drop only, we might not need the "FERNOBRIX" there but that's up to the designer), and we want to have a lot of white space so people can make notes on this when decided (though we don't need lines on the back for writing or so).

```html
<!DOCTYPE html>
<html lang="en">
<head>
<meta charset="utf-8">
<title>Fernobrix Stationery</title>
<link href="https://fonts.googleapis.com/css2?family=Open+Sans:wght@400;600;700&display=swap" rel="stylesheet">
<style>
  :root {
    --teal: #2aa9b8;
    --teal-light: #7fd0d9;
    --teal-pale: #e3f4f6;
    --navy: #1d3a78;
    --ink: #4a4f57;
    --paper: #ffffff;
    --bg: #ffffff;
  }
  * { box-sizing: border-box; margin: 0; padding: 0; }
  html, body { width: 1200px; height: 857px; overflow: hidden; background: var(--bg); }
  body { position: relative; font-family: "Open Sans", Arial, sans-serif; color: var(--ink); }

  .sheet { position: absolute; background: var(--paper); box-shadow: 0 1px 5px rgba(0,0,0,.2); overflow: hidden; }
  .sheet > svg.art { position: absolute; left: 0; top: 0; width: 100%; height: 100%; }

  .wordmark { position: absolute; display: flex; align-items: center; gap: 6px;
    font-weight: 700; color: var(--navy); letter-spacing: .3px; line-height: 1; white-space: nowrap; }
  .wordmark .dot { border-radius: 50%; background: var(--teal); flex: none; }

  /* Letterhead */
  .letterhead { left: 12px; top: 12px; width: 636px; height: 828px; }
  .letterhead .wordmark { left: 28px; top: 98px; font-size: 26px; }
  .letterhead .wordmark .dot { width: 17px; height: 17px; }
  .letterhead .footer { position: absolute; right: 28px; bottom: 20px; font-size: 8px; white-space: nowrap; }

  /* Envelope */
  .envelope { left: 497px; top: 245px; width: 679px; height: 374px; }
  .envelope .wordmark { left: 20px; top: 76px; font-size: 24px; }
  .envelope .wordmark .dot { width: 16px; height: 16px; }
  .envelope .return { position: absolute; left: 22px; top: 108px; font-size: 8px; white-space: nowrap; }
  .envelope .window { position: absolute; left: 122px; top: 163px; width: 226px; height: 96px;
    border: 1px solid #c9ccd0; border-radius: 6px; background: #f0f1f2; }

  /* Business cards */
  .card { top: 648px; width: 247px; height: 168px; }
  .card-front { left: 665px; }
  .card-front .wordmark { left: 10px; top: 30px; font-size: 15px; gap: 4px; }
  .card-front .wordmark .dot { width: 9px; height: 9px; }
  .card-front .person { position: absolute; left: 12px; top: 66px; }
  .card-front .name { font-size: 11px; font-weight: 700; color: var(--navy); white-space: nowrap; }
  .card-front .role { font-size: 6px; }
  .card-front .contact { position: absolute; left: 150px; top: 64px; font-size: 5.5px; line-height: 1.35; white-space: nowrap; }
  .card-back { left: 926px; width: 250px; }
  .card-back .mark { position: absolute; left: 105px; top: 50px; width: 44px; height: 44px;
    border-radius: 50%; background: var(--teal); opacity: .85; }
</style>
</head>
<body>

<section class="sheet letterhead" aria-label="Letterhead">
  <svg class="art" viewBox="0 0 636 828" preserveAspectRatio="none" aria-hidden="true">
    <defs>
      <linearGradient id="lhTeal" x1="0" y1="0" x2="1" y2="0">
        <stop offset="0" stop-color="#ffffff"/><stop offset=".35" stop-color="#7fd0d9"/><stop offset="1" stop-color="#2aa9b8"/>
      </linearGradient>
    </defs>
    <path d="M0 0H636V190C480 120 260 70 0 62Z" fill="url(#lhTeal)"/>
    <path d="M0 66C260 74 480 124 636 196" stroke="#1d3a78" stroke-width="3" fill="none"/>
  </svg>
  <div class="wordmark"><span class="dot"></span>FERNOBRIX</div>
  <p class="footer">4273 Beldon Street, Larkview, ON, K4V 7N2 Canada | Phone: 1 555 210 0148 | www.fernobrix.com</p>
</section>

<section class="sheet envelope" aria-label="Envelope">
  <svg class="art" viewBox="0 0 679 374" preserveAspectRatio="none" aria-hidden="true">
    <defs>
      <linearGradient id="envTeal" x1="0" y1="0" x2="1" y2="0">
        <stop offset="0" stop-color="#ffffff"/><stop offset=".3" stop-color="#7fd0d9"/><stop offset="1" stop-color="#2aa9b8"/>
      </linearGradient>
    </defs>
    <path d="M0 0H679V92C500 56 280 38 0 36Z" fill="url(#envTeal)"/>
    <path d="M0 40C280 42 500 62 679 98" stroke="#1d3a78" stroke-width="3" fill="none"/>
  </svg>
  <div class="wordmark"><span class="dot"></span>FERNOBRIX</div>
  <p class="return">4273 Beldon Street, Larkview, ON, K4V 7N2 Canada</p>
  <div class="window"></div>
</section>

<section class="sheet card card-front" aria-label="Business card front">
  <svg class="art" viewBox="0 0 247 168" preserveAspectRatio="none" aria-hidden="true">
    <defs>
      <linearGradient id="cardTeal" x1="0" y1="0" x2="1" y2="0">
        <stop offset="0" stop-color="#ffffff"/><stop offset=".3" stop-color="#7fd0d9"/><stop offset="1" stop-color="#2aa9b8"/>
      </linearGradient>
    </defs>
    <path d="M0 0H247V46C180 28 100 20 0 22Z" fill="url(#cardTeal)"/>
    <path d="M0 25C100 24 180 32 247 50" stroke="#1d3a78" stroke-width="2" fill="none"/>
    <path d="M0 168V140C90 126 170 120 247 124V168Z" fill="url(#cardTeal)"/>
    <path d="M0 137C90 123 170 117 247 121" stroke="#1d3a78" stroke-width="1.5" fill="none"/>
  </svg>
  <div class="wordmark"><span class="dot"></span>FERNOBRIX</div>
  <div class="person">
    <p class="name">Martin Doyle</p>
    <p class="role">President &amp; CEO</p>
  </div>
  <p class="contact">4273 Beldon Street<br>Larkview, ON<br>K4V 7N2 Canada<br>Phone: 1 555 210 0148<br>Email: mdoyle@fernobrix.com<br>www.fernobrix.com</p>
</section>

<section class="sheet card card-back" aria-label="Business card back">
  <svg class="art" viewBox="0 0 250 168" preserveAspectRatio="none" aria-hidden="true">
    <defs>
      <linearGradient id="backWash" x1="0" y1="0" x2="1" y2="0">
        <stop offset="0" stop-color="#ffffff"/><stop offset=".5" stop-color="#e3f4f6"/><stop offset="1" stop-color="#c6e8ec"/>
      </linearGradient>
    </defs>
    <rect width="250" height="168" fill="url(#backWash)"/>
  </svg>
  <div class="mark"></div>
</section>

</body>
</html>
```